Brook Forge - Crypto Currency Miner Powered by Renewable Energy Website

We Need Web Pages Design for Website for Crypto Currency Miner

Serivices include:
Mining Rig Sales
Housing for Rigs turnkey on renewable energy grid
Cloud Mining term packages
Updates

http://www.vaultrigratings.example (Competitors sites)

Target Market(s)

Investers for Mining Rigs and terms for 1,2 or 3 years of Hash rate

Industry/Entity Type

Mining

Number of Pages Required

5+ page

Font styles to use
Sans Serif

Colors
add136
9bcb3c
606060
474747
ffc214
cadf82
fbee3e
876aae
6b449b

Requirements
Must have
• Pictures of Solar, Wind and power Factor Correction units
Nice to have
• e-commerce platform so contract terms can be purchased through website
Should not have
• Heavy construction equipment

```html
<!DOCTYPE html>
<html lang="en">
<head>
<meta charset="utf-8">
<title>Brook Forge – Renewable Crypto Mining</title>
<link rel="stylesheet" href="https://fonts.googleapis.com/css2?family=Open+Sans:wght@300;400;600;700;800&display=swap">
<style>
:root{
  --green:#14953a;
  --green-mid:#2f9a3c;
  --green-light:#7cba35;
  --green-strip:#4aa33a;
  --accent:#f28c1c;
  --gray:#8a8a8a;
  --gray-dark:#474747;
  --text:#333;
  --section:#ededf2;
  --white:#fff;
  --star:#f0a30a;
  --link-blue:#2a9ad6;
}
*{box-sizing:border-box;margin:0;padding:0}
html,body{width:1200px;height:2970px;overflow:hidden}
body{position:relative;font-family:"Open Sans",Arial,sans-serif;color:var(--text);background:var(--section)}
.abs{position:absolute}

/* header */
.topline{left:0;top:0;width:1200px;height:4px;background:var(--accent)}
.header{left:0;top:4px;width:1200px;height:126px;background:var(--white)}
.brand{left:80px;top:42px;display:flex;align-items:center;gap:12px}
.brand-dot{width:60px;height:60px;border-radius:50%;background:var(--green)}
.brand-name{font-size:40px;font-weight:700;color:var(--green-mid);letter-spacing:-.5px;white-space:nowrap}
.search{left:465px;top:42px;width:436px;height:48px;border-radius:24px;background:#ececf0;display:flex;align-items:center;padding:0 20px;font-size:13px;color:#999;justify-content:space-between}
.util{top:38px;width:70px;text-align:center;font-size:11px;color:#666}
.util svg{display:block;margin:0 auto 6px}

/* nav */
.nav{left:0;top:130px;width:1200px;height:48px;background:var(--green);color:#fff;font-size:14px;font-weight:600}
.nav-item{top:0;height:48px;line-height:48px;white-space:nowrap}
.nav-active{left:224px;width:133px;background:#2aa54a;padding-left:20px}
.caret{display:inline-block;margin-left:16px;border:5px solid transparent;border-top-color:#fff;vertical-align:-2px}

/* hero */
.hero{left:0;top:178px;width:1200px;height:462px;background:linear-gradient(100deg,#f4c25a 0%,#e9a43b 14%,#c98f4a 24%,#a8b6c8 40%,#6f89a8 60%,#3e5d86 80%,#2c4a74 100%)}
.hero-title{left:72px;top:296px;font-size:72px;font-weight:400;color:#111;line-height:1;white-space:nowrap}
.hero-title b{font-weight:800}
.hero-sub{left:75px;top:384px;font-size:21px;color:#111;font-weight:400;white-space:nowrap}
.hero-note{left:75px;top:422px;font-size:11px;font-weight:700;color:#111;white-space:nowrap}
.hero-btn{left:77px;top:467px;width:157px;height:44px;background:#111;color:#fff;font-size:16px;line-height:44px;text-align:center;border-radius:2px}

/* feature strip */
.strip{top:640px;height:65px;display:flex;align-items:center;color:#fff;font-size:17px;font-weight:600;gap:18px;white-space:nowrap}
.strip-a{left:0;width:424px;background:var(--gray);padding-left:100px}
.strip-b{left:424px;width:346px;background:var(--gray-dark);padding-left:40px}
.strip-c{left:770px;width:430px;background:var(--green-strip);padding-left:40px}

/* products */
.section-title{left:0;width:1200px;text-align:center;font-size:31px;font-weight:400;color:#222}
.product{top:877px;width:333px;height:258px;background:#fff;box-shadow:0 1px 4px rgba(0,0,0,.12)}
.product-img{left:0;top:0;width:166px;height:258px;background:linear-gradient(180deg,#8fc6ee 0%,#5aa0d8 45%,#6fb33e 70%,#e8c3a2 100%)}
.product-info{left:166px;top:0;width:167px;height:258px;text-align:center}
.product-name{margin-top:40px;font-size:12px;font-weight:600;color:#555}
.rating{margin-top:10px;font-size:16px;color:#555}
.stars{font-size:15px;color:var(--star);letter-spacing:1px;margin-top:6px}
.reviews{font-size:11px;color:#999;margin-top:6px}
.price{font-size:21px;color:#222;margin-top:10px}
.cart-btn{left:166px;top:258px;width:167px;height:45px;line-height:45px;text-align:center;color:#fff;font-size:12px}

/* solutions */
.solutions{left:0;top:1269px;width:1200px;height:598px;background:linear-gradient(180deg,#5c6770 0%,#3d4e62 40%,#2b4470 70%,#20365e 100%)}
.solutions-title{top:1316px;color:#fff}
.sol-card{top:1398px;width:341px;height:356px;text-align:center;padding-top:28px}
.sol-card h3{font-size:17px;font-weight:700;margin-top:26px}
.sol-card p{font-size:14px;line-height:18px;margin:26px auto 0;width:280px;height:54px}
.sol-btn{display:inline-block;margin-top:40px;width:102px;height:32px;line-height:30px;font-size:12px;border:1px solid}
.sol-1{left:77px;background:var(--green-light);color:#fff}
.sol-2{left:430px;background:#f2f2f2;color:#333}
.sol-2 h3{color:var(--link-blue)}
.sol-2 .sol-btn{color:#888;border-color:#999}
.sol-3{left:782px;background:var(--green);color:#fff}
.dots{left:566px;top:1800px;display:flex;gap:12px}
.dot{width:14px;height:14px;border-radius:50%;border:2px solid #cfd6de}
.dot.on{background:#fff;border-color:#fff}

/* testimonials */
.people{left:77px;top:2051px;width:1046px;height:167px;display:flex}
.person{flex:1;height:167px}
.person-1{background:linear-gradient(180deg,#8a8a8a,#5c5c5c)}
.person-2{background:linear-gradient(180deg,#d0d0d0,#777)}
.person-3{background:linear-gradient(180deg,#6f6f6f,#3f3f3f)}
.person-4{background:linear-gradient(180deg,#c96f54,#3aa6c9)}
.reviewer{left:77px;top:2256px;width:300px;text-align:center}
.reviewer-name{font-size:30px;font-weight:700;color:#444;letter-spacing:.5px;white-space:nowrap}
.reviewer-role{font-size:13px;color:#555;margin-top:8px}
.quote{left:390px;top:2256px;width:710px;font-size:15px;line-height:22px;color:#666;font-weight:300}
.reviews-btn{left:390px;top:2378px;width:176px;height:36px;line-height:36px;background:var(--green);color:#fff;text-align:center;font-size:12px;font-weight:700}

/* footer */
.footer{left:0;top:2505px;width:1200px;height:400px;background:#fff}
.foot-brand{left:80px;top:2590px;display:flex;align-items:center;gap:10px}
.foot-brand .brand-dot{width:50px;height:50px}
.foot-brand .brand-name{font-size:33px}
.foot-contact{left:77px;top:2672px;font-size:12px;line-height:27px;color:#444}
.foot-h{top:2600px;font-size:15px;font-weight:600;color:#444}
.foot-about{left:430px;top:2652px;width:245px;font-size:12px;line-height:17px;color:#777}
.foot-links{left:709px;top:2650px;font-size:12px;line-height:28px;color:#555;list-style:none}
.foot-sub{left:905px;top:2650px;width:230px;font-size:12px;line-height:17px;color:#666}
.email{left:905px;top:2711px;width:218px;height:35px;border:1px solid #aaa;display:flex;align-items:center;gap:10px;padding-left:14px;font-size:12px;color:#999}
.submit{left:905px;top:2764px;width:111px;height:30px;line-height:30px;background:var(--green);color:#fff;text-align:center;font-size:12px}
.bottom{left:0;top:2905px;width:1200px;height:65px;background:var(--green);color:#fff;font-size:12px}
.bottom-text{left:77px;top:24px}
.social{top:18px;width:28px;height:28px;border-radius:50%;border:2px solid #fff}
</style>
</head>
<body>
<div class="abs topline"></div>
<header class="abs header"></header>
<div class="abs brand"><span class="brand-dot"></span><span class="brand-name">Brook Forge</span></div>
<div class="abs search"><span>Search rigs and terms...</span>
  <svg width="18" height="18" viewBox="0 0 18 18"><circle cx="7.5" cy="7.5" r="5.5" fill="none" stroke="#777" stroke-width="2"/><line x1="11.5" y1="11.5" x2="16" y2="16" stroke="#777" stroke-width="2"/></svg></div>
<div class="abs util" style="left:920px"><svg width="28" height="28" viewBox="0 0 28 28"><circle cx="14" cy="14" r="12" fill="none" stroke="#2aa54a" stroke-width="2"/><circle cx="14" cy="11" r="4" fill="#2aa54a"/><path d="M7 21c2-4 12-4 14 0" fill="#2aa54a"/></svg>Login</div>
<div class="abs util" style="left:992px"><svg width="28" height="28" viewBox="0 0 28 28"><path d="M5 16v-3a9 9 0 0 1 18 0v3" fill="none" stroke="#2aa54a" stroke-width="2"/><rect x="3" y="14" width="5" height="8" rx="2" fill="#2aa54a"/><rect x="20" y="14" width="5" height="8" rx="2" fill="#2aa54a"/></svg>Support</div>
<div class="abs util" style="left:1064px"><svg width="32" height="28" viewBox="0 0 32 28"><path d="M2 8h5l4 13h14l3-9H9" fill="none" stroke="#555" stroke-width="2"/><circle cx="13" cy="25" r="2" fill="#555"/><circle cx="23" cy="25" r="2" fill="#555"/><circle cx="22" cy="7" r="7" fill="#2aa54a"/><text x="22" y="10" font-size="9" fill="#fff" text-anchor="middle" font-family="Open Sans,sans-serif">5</text></svg>Checkout</div>

<nav class="abs nav">
  <div class="abs nav-item" style="left:77px">Mining Rigs<span class="caret"></span></div>
  <div class="abs nav-item nav-active">Services<span class="caret"></span></div>
  <div class="abs nav-item" style="left:388px">About us</div>
  <div class="abs nav-item" style="left:532px">Updates</div>
  <div class="abs nav-item" style="left:1048px">Store <svg width="20" height="20" viewBox="0 0 20 20" style="vertical-align:-4px;margin-left:6px"><circle cx="10" cy="10" r="9" fill="#fff"/></svg></div>
</nav>

<div class="abs hero" role="img" aria-label="Rows of solar panels in a field at sunset"></div>
<h1 class="abs hero-title">Clean <b>Hashpower</b></h1>
<p class="abs hero-sub">MINING RIGS RUNNING ON SOLAR AND WIND ENERGY</p>
<p class="abs hero-note">TURNKEY RIG HOUSING ON A RENEWABLE GRID. &nbsp; | &nbsp; CLOUD TERMS OF 1, 2 OR 3 YEARS</p>
<div class="abs hero-btn">Get Started</div>

<div class="abs strip strip-a"><svg width="30" height="30" viewBox="0 0 30 30"><rect x="3" y="5" width="24" height="22" fill="none" stroke="#fff" stroke-width="2"/><line x1="3" y1="11" x2="27" y2="11" stroke="#fff" stroke-width="2"/><text x="15" y="24" font-size="10" fill="#fff" text-anchor="middle" font-family="Open Sans,sans-serif">30</text></svg>30 Days Money Back</div>
<div class="abs strip strip-b"><svg width="38" height="38" viewBox="0 0 38 38"><circle cx="19" cy="19" r="17" fill="#fff"/><text x="19" y="23" font-size="10" font-weight="700" fill="#474747" text-anchor="middle" font-family="Open Sans,sans-serif">24/7</text></svg>1 Year Free Support</div>
<div class="abs strip strip-c"><svg width="34" height="34" viewBox="0 0 34 34"><path d="M6 17a11 11 0 1 0 3-7.6" fill="none" stroke="#fff" stroke-width="2"/><path d="M5 5v6h6" fill="none" stroke="#fff" stroke-width="2"/><path d="M17 10v7l5 3" fill="none" stroke="#fff" stroke-width="2"/></svg>Free Rig Installation</div>

<h2 class="abs section-title" style="top:776px">Our Best Selling Mining Rigs</h2>

<div class="abs product" style="left:75px">
  <div class="abs product-img" role="img" aria-label="Solar panel and wind turbine held in open hands"></div>
  <div class="abs product-info"><div class="product-name">Rig + 1 Year Hosting</div><div class="rating">5.0</div><div class="stars">★★★★★</div><div class="reviews">100 Reviews</div><div class="price">$11129.00</div></div>
  <div class="abs cart-btn" style="background:#8a8a8a">Add To Cart</div>
</div>
<div class="abs product" style="left:434px">
  <div class="abs product-img" role="img" aria-label="Solar panel and wind turbine held in open hands"></div>
  <div class="abs product-info"><div class="product-name">Rig + 2 Year Hosting</div><div class="rating">5.0</div><div class="stars">★★★★★</div><div class="reviews">100 Reviews</div><div class="price">$11129.00</div></div>
  <div class="abs cart-btn" style="background:#474747">Add To Cart</div>
</div>
<div class="abs product" style="left:792px">
  <div class="abs product-img" role="img" aria-label="Solar panel and wind turbine held in open hands"></div>
  <div class="abs product-info"><div class="product-name">Rig + 3 Year Hosting</div><div class="rating">5.0</div><div class="stars">★★★★★</div><div class="reviews">100 Reviews</div><div class="price">$11129.00</div></div>
  <div class="abs cart-btn" style="background:var(--green)">Add To Cart</div>
</div>

<div class="abs solutions" role="img" aria-label="Solar farm with wind turbines under a dusky sky"></div>
<h2 class="abs section-title solutions-title">Quick Solutions</h2>
<div class="abs sol-card sol-1">
  <svg width="90" height="60" viewBox="0 0 90 60"><path d="M25 50L70 12M52 10h20v20" fill="none" stroke="#fff" stroke-width="3"/><line x1="10" y1="30" x2="30" y2="30" stroke="#fff" stroke-width="2"/><line x1="14" y1="40" x2="34" y2="40" stroke="#fff" stroke-width="2"/></svg>
  <h3>Mining Rig Sales</h3>
  <p>Buy tested, efficient mining rigs shipped ready to hash or installed straight into our renewable farm</p>
  <span class="sol-btn">Read More</span>
</div>
<div class="abs sol-card sol-2">
  <svg width="90" height="60" viewBox="0 0 90 60"><path d="M40 4l18 6v16c0 14-9 22-18 26-9-4-18-12-18-26V10z" fill="none" stroke="#7cba35" stroke-width="3"/><path d="M32 26l6 6 10-12" fill="none" stroke="#7cba35" stroke-width="3"/><rect x="52" y="40" width="16" height="13" fill="#7cba35"/><path d="M55 40v-4a5 5 0 0 1 10 0v4" fill="none" stroke="#7cba35" stroke-width="2"/></svg>
  <h3>Turnkey Rig Housing</h3>
  <p>Secure, cooled housing for your rigs on a solar and wind grid with power factor correction</p>
  <span class="sol-btn">Read More</span>
</div>
<div class="abs sol-card sol-3">
  <svg width="90" height="60" viewBox="0 0 90 60"><path d="M24 6h16l5 6h21v42H24z" fill="none" stroke="#fff" stroke-width="3"/><line x1="24" y1="18" x2="66" y2="18" stroke="#fff" stroke-width="3"/></svg>
  <h3>Cloud Mining Terms</h3>
  <p>Lease fixed hash rate for 1, 2 or 3 years and receive daily payouts with no hardware to run</p>
  <span class="sol-btn">Read More</span>
</div>
<div class="abs dots"><span class="dot"></span><span class="dot on"></span><span class="dot"></span></div>

<h2 class="abs section-title" style="top:1948px">1000 Investors run their hash rate on clean energy</h2>
<div class="abs people">
  <div class="person person-1" role="img" aria-label="Portrait of a smiling woman outdoors, greyscale"></div>
  <div class="person person-2" role="img" aria-label="Portrait of a young man with a backpack, greyscale"></div>
  <div class="person person-3" role="img" aria-label="Portrait of a man wearing glasses, greyscale"></div>
  <div class="person person-4" role="img" aria-label="Portrait of a smiling man in a blue shirt"></div>
</div>
<div class="abs reviewer"><div class="reviewer-name">DALE MORROW</div><div class="reviewer-role">CEO AND CTO</div></div>
<p class="abs quote">We moved our whole fleet of mining rigs into Brook Forge housing and signed a three year cloud term for extra hash rate. Uptime has been steady, the solar and wind supply keeps our power cost low and predictable, and the payout dashboard shows every coin we earn. It is the simplest way we have found to mine with clean energy.</p>
<div class="abs reviews-btn">VIEW ALL REVIEWS</div>

<footer class="abs footer"></footer>
<div class="abs foot-brand"><span class="brand-dot"></span><span class="brand-name">Brook Forge</span></div>
<div class="abs foot-contact">214 Linden Terrace, Ridge Road, USA<br>Call: &nbsp;1800 55501 23<br>Mail: hello@brookforge.example</div>
<h4 class="abs foot-h" style="left:430px">About Us</h4>
<p class="abs foot-about">Brook Forge sells crypto mining rigs, houses them turnkey on a renewable energy grid and offers cloud mining terms of one, two or three years, so investors can earn hash rate powered by solar and wind.</p>
<h4 class="abs foot-h" style="left:709px">Discover</h4>
<ul class="abs foot-links"><li>Mining Rigs</li><li>Faq</li><li>Rig Housing</li><li>Cloud Mining Terms</li><li>Terms and Policy</li><li>Contract Policy</li><li>Updates</li></ul>
<h4 class="abs foot-h" style="left:905px">Subscribe with us</h4>
<p class="abs foot-sub">Sign up for our mailing list to get mining updates and offers</p>
<div class="abs email"><svg width="18" height="12" viewBox="0 0 18 12"><rect x="1" y="1" width="16" height="10" fill="none" stroke="#999"/><path d="M1 1l8 6 8-6" fill="none" stroke="#999"/></svg>Email Address</div>
<div class="abs submit">Submit</div>

<div class="abs bottom">
  <span class="abs bottom-text">(c) powered by northpixel.example</span>
  <span class="abs social" style="left:990px"></span>
  <span class="abs social" style="left:1028px"></span>
  <span class="abs social" style="left:1066px"></span>
  <span class="abs social" style="left:1104px"></span>
</div>
</body>
</html>
```